Awesome Business Card Design needed!

Hey there.
I'm looking for a simple but awesome business card design.
Type of company: Online advertisement agency
(please don't use the typical business people or statistics images on the card)
The front has to display the business name
and possibly some sort of logo ( perhaps something with the two M's of the biz name )
And the back of the card should say:
Name
Phone
Email
Let your imagination flow.
here are some designs that I like and that you can use as inspiration.
Simple but Awesome
http://images.pixelvane.example/designs/55128_877673_43091_thumbnail.jpg
http://images.pixelvane.example/designs/37714_747642_40106_image.jpg
http://images.pixelvane.example/designs/55128_877673_43091_image.jpg
http://images.pixelvane.example/designs/51321_781878_43091_image.jpg
http://images.pixelvane.example/designs/33378_399063_15912_image.jpg
http://images.pixelvane.example/designs/2337_271604_9495_image.jpg
good luck

```html
<!DOCTYPE html>
<html lang="en">
<head>
<meta charset="utf-8">
<title>Corvane Media – Business Card</title>
<link href="https://fonts.googleapis.com/css2?family=Arimo:wght@400;700&display=swap" rel="stylesheet">
<style>
  :root {
    --stage: #262626;
    --front-bg: #f2f2f2;
    --front-edge: #d9d9d9;
    --back-top: #1b2536;
    --back-bottom: #000000;
    --ink-dark: #1a1a1a;
    --ink-light: #ffffff;
    --accent-blue: #1f9ad6;
    --tone-green: #3cc82a;
    --tone-blue: #2a8fd6;
    --tone-yellow: #f4c21a;
  }
  * { box-sizing: border-box; margin: 0; padding: 0; }
  html, body { width: 1200px; height: 900px; overflow: hidden; }
  body {
    background: var(--stage);
    font-family: "Arimo", Arial, sans-serif;
    position: relative;
  }
  .card {
    position: absolute;
    left: 272px;
    width: 654px;
    height: 378px;
    overflow: hidden;
  }
  .card--front {
    top: 60px;
    background: radial-gradient(ellipse at 50% 30%, #ffffff 0%, var(--front-bg) 60%, var(--front-edge) 100%);
  }
  .card--back {
    top: 460px;
    background: radial-gradient(ellipse at 5% 5%, var(--back-top) 0%, #0b0f18 45%, var(--back-bottom) 80%);
  }
  .accent-band {
    position: absolute;
    left: 0; bottom: 0;
    width: 100%;
    height: 10px;
    background: linear-gradient(90deg, var(--tone-green), var(--tone-blue) 50%, var(--tone-yellow));
  }
  .corner-art {
    position: absolute;
    top: 0;
    width: 114px;
    height: 114px;
    background: linear-gradient(135deg, var(--tone-green), var(--tone-blue) 55%, var(--tone-yellow));
  }
  .card--front .corner-art { left: 0; clip-path: polygon(0 0, 100% 0, 0 100%); }
  .card--back .corner-art { right: 0; clip-path: polygon(0 0, 100% 0, 100% 100%); }
  .brand-name {
    position: absolute;
    top: 280px;
    left: 0;
    width: 100%;
    text-align: center;
    font-weight: 700;
    font-size: 32px;
    letter-spacing: 1px;
    color: var(--ink-dark);
  }
  .card--front .brand-name { top: 220px; }
  .contact {
    position: absolute;
    top: 134px;
    left: 0;
    width: 100%;
    text-align: center;
    color: var(--ink-light);
  }
  .contact-name {
    font-weight: 700;
    font-size: 33px;
    line-height: 38px;
    text-decoration: underline;
    text-underline-offset: 4px;
    text-decoration-thickness: 2px;
  }
  .contact-role {
    margin-top: 2px;
    font-weight: 700;
    font-size: 24px;
    color: var(--accent-blue);
  }
  .contact-lines {
    margin-top: 34px;
    font-size: 15px;
    line-height: 30px;
  }
  .contact-lines .label { color: var(--accent-blue); margin-right: 8px; }
</style>
</head>
<body>

<section class="card card--front">
  <div class="corner-art" role="img" aria-label="Peeled corner revealing colourful tiles"></div>
  <h1 class="brand-name">CORVANE MEDIA</h1>
  <div class="accent-band" role="img" aria-label="Multicolour accent band"></div>
</section>

<section class="card card--back">
  <div class="corner-art" role="img" aria-label="Peeled corner revealing colourful tiles"></div>
  <div class="contact">
    <h2 class="contact-name">YOUR NAME</h2>
    <p class="contact-role">CEO</p>
    <div class="contact-lines">
      <p><span class="label">P</span>: 123 456</p>
      <p><span class="label">E</span>: info@CorvaneMedia.com</p>
    </div>
  </div>
  <div class="accent-band" role="img" aria-label="Multicolour accent band"></div>
</section>

</body>
</html>
```